New Business Card Design Project

I would like a business card to match my truck wrap and logo. I would like the font to match my existing business card please.

Industry/Entity Type

Painter

Contact Information for Business Card

Rodrigo Venter 801-437-2910 Ventercoatings.utah@brushmail.net
SERVICES - Custom Paint & Stain, Interior & Exterior, Epoxy Coatings / Garage Floors, Cabinet Refinishing, Log Staining and Refinishing.

Requirements
Nice to have
• I would like to have the white and grey line like the bottom of my vehicle wrap, Light Grey to match my truck also.

```html
<!DOCTYPE html>
<html lang="en">
<head>
<meta charset="UTF-8">
<title>Venter Coatings – Business Card</title>
<link href="https://fonts.googleapis.com/css2?family=Arimo:wght@400;700&display=swap" rel="stylesheet">
<style>
:root{
  --bg:#2b2b2d;
  --card:#ffffff;
  --blue:#1f74c2;
  --blue-light:#2d9be0;
  --grey-text:#8a8d93;
  --band:#a3a7b0;
  --band-light:#c4c7ce;
  --divider:#b9bcc2;
}
*{margin:0;padding:0;box-sizing:border-box}
html,body{width:1200px;height:900px;overflow:hidden;background:var(--bg);font-family:"Arimo",Arial,sans-serif}
.canvas{position:relative;width:1200px;height:900px}
.card{position:absolute;left:300px;width:600px;height:343px;background:var(--card);border-radius:22px;overflow:hidden}
.card--back{top:55px}
.card--front{top:480px}

/* brand lockup */
.brand{position:absolute;display:flex;align-items:center;gap:14px}
.brand__mark{width:42px;height:42px;background:var(--blue);border-radius:4px}
.brand__name{color:var(--blue);font-weight:700;font-size:30px;line-height:1;letter-spacing:1px}
.brand__sub{display:block;font-size:13px;letter-spacing:9px;margin-top:6px}

/* services list */
.services{position:absolute;color:var(--grey-text);font-size:16px;line-height:22px;list-style:none;white-space:nowrap}
.services__title{color:var(--blue);font-weight:700;font-size:25px;line-height:29px;letter-spacing:.5px;margin-bottom:2px}

/* back */
.card--back .brand{left:50px;top:145px}
.back__divider{position:absolute;left:296px;top:75px;width:1px;height:195px;background:var(--divider)}
.card--back .services{left:318px;top:95px}
.card--back .services__title{margin-left:15px}
.card--back .services li:not(.services__title)::before{content:"";display:inline-block;width:7px;height:7px;border-radius:50%;background:var(--blue-light);margin-right:8px;vertical-align:middle}

/* front */
.front__band{position:absolute;left:0;top:0}
.front__name{position:absolute;left:34px;top:30px;color:var(--blue);font-weight:700;font-size:22px;letter-spacing:1px}
.card--front .brand{left:40px;top:185px}
.card--front .services{right:36px;top:22px;text-align:right}
.card--front .services li::after{content:"";display:inline-block;width:7px;height:7px;border-radius:50%;background:var(--blue-light);margin-left:8px;vertical-align:middle}
.contact{position:absolute;right:30px;top:228px;text-align:right;color:#fff;font-size:15px;line-height:26px;list-style:none;white-space:nowrap}
.contact li{display:flex;align-items:center;justify-content:flex-end;gap:8px}
.contact svg{width:14px;height:14px}
</style>
</head>
<body>
<div class="canvas">

  <section class="card card--back">
    <div class="brand">
      <span class="brand__mark"></span>
      <span class="brand__name">VENTER<span class="brand__sub">COATINGS</span></span>
    </div>
    <div class="back__divider"></div>
    <ul class="services">
      <li class="services__title">SERVICES</li>
      <li>Custom Paint &amp; Stain</li>
      <li>Interior &amp; Exterior</li>
      <li>Epoxy Coatings / Garage Floors</li>
      <li>Cabinet Refinishing</li>
      <li>Log Staining and Refinishing.</li>
    </ul>
  </section>

  <section class="card card--front">
    <svg class="front__band" width="600" height="343" viewBox="0 0 600 343">
      <polygon points="0,304 270,276 305,217 600,192 600,343 0,343" fill="var(--band)"/>
      <polyline points="0,294 263,266 298,207 600,182" fill="none" stroke="var(--band-light)" stroke-width="4"/>
    </svg>
    <div class="front__name">RODRIGO VENTER</div>
    <div class="brand">
      <span class="brand__mark"></span>
      <span class="brand__name">VENTER<span class="brand__sub">COATINGS</span></span>
    </div>
    <ul class="services">
      <li class="services__title">SERVICES</li>
      <li>Custom Paint &amp; Stain</li>
      <li>Interior &amp; Exterior</li>
      <li>Epoxy Coatings / Garage Floors</li>
      <li>Cabinet Refinishing</li>
      <li>Log Staining and Refinishing</li>
    </ul>
    <ul class="contact">
      <li>801-437-2910
        <svg viewBox="0 0 24 24"><path d="M6.6 10.8a15 15 0 0 0 6.6 6.6l2.2-2.2a1 1 0 0 1 1-.25 11.4 11.4 0 0 0 3.6.57 1 1 0 0 1 1 1V20a1 1 0 0 1-1 1A17 17 0 0 1 3 4a1 1 0 0 1 1-1h3.5a1 1 0 0 1 1 1c0 1.25.2 2.45.57 3.57a1 1 0 0 1-.25 1z" fill="#fff"/></svg>
      </li>
      <li>Ventercoatings.utah@brushmail.net
        <svg viewBox="0 0 24 24"><rect x="2.5" y="5" width="19" height="14" rx="1" fill="none" stroke="#fff" stroke-width="2"/><polyline points="3,6 12,13 21,6" fill="none" stroke="#fff" stroke-width="2"/></svg>
      </li>
    </ul>
  </section>

</div>
</body>
</html>
```